Australian Consultant Pharmacist Business Needs A3 Flyer for Medical Centre

Our business has just secured a deal in a medical centre to offer our consulting services. We have installed our software on the doctors computers and would like to have an A3 flyer to put on their walls to remind them about our services and explain very briefly how to use our simple software.

We would like the flyer to be vibrant and very simple whilst conveying our message of improving patient health outcomes and illustrating how to use our software and service.

We provide Home Medicine Reviews (HMR) for General Practitioners (GP) at medical centres.

There are 3 pathways for a GP to use our service, all resulting in the same outcome.

The outcome is the Dr sends us a referral for a HMR for their patient. In turn they receive a report back after we have performed the HMR.

Pathways
1.
-GP Opens Patient File in medical prescribing software
-If patient is eligible for a HMR, an alert will pop up in bottom right hand corner (approx 30 seconds)
- Click Send Referral
- New page opens, select reason for referral ie. several medicines
- Press Send - referral is sent electronically to Pharmacist

2.
No alert pops up but GP still wants to refer.
Right click RX Notify program - RX Notify program is identified by the bell shape icon in the bottom right side of the desktop tray next to the time.
Click refer current patient - this will refer the patient currently open on the GP prescribing software

3. GP would like to send HMR Referal via Fax.
Fax number 03 9172 3408

I have attached some examples of how the software and service works, including screen shots and some power points. I would like to use these as ideas for our A3 Flyer.

Good Luck!

Target Market(s)

Doctors

Industry/Entity Type

Health Service

Colors
f37122
0455a3
3176b5
33a6d7
f68d4c

Requirements
Must have
• Our company name - Brightpath Care HMR
• Our email brightpathcarehmr@mailvista.example
• our fax number
• the 3 ways to use our service and how
• prefer images and short keyword descriptions
• convey idea of improving patient health
• ensure our service comes accross as simple and effecient
Nice to have
• images, vibrant,
Should not have
• lengthy descriptions

```html
<!DOCTYPE html>
<html lang="en">
<head>
<meta charset="utf-8">
<title>Brightpath Care HMR – How to use our services</title>
<link rel="stylesheet" href="https://fonts.googleapis.com/css2?family=Anton&family=Lato:ital,wght@0,300;0,400;0,700;1,400&display=swap">
<style>
  :root {
    --orange: #f37122;
    --orange-soft: #f68d4c;
    --navy: #0455a3;
    --blue: #3176b5;
    --sky: #33a6d7;
    --mist: #dadee3;
    --panel: #c9ced4;
    --white: #ffffff;
  }
  * { margin: 0; padding: 0; box-sizing: border-box; }
  html, body { width: 849px; height: 1200px; overflow: hidden; background: var(--blue); }
  .flyer {
    position: relative; width: 849px; height: 1200px; overflow: hidden;
    font-family: "Lato", sans-serif; color: var(--white);
  }
  .backdrop { position: absolute; inset: 0; }
  .title {
    position: absolute; top: 18px; left: 0; width: 849px; text-align: center;
    font-family: "Anton", sans-serif; font-size: 58px; letter-spacing: 1px;
    text-shadow: 2px 2px 0 rgba(0,0,0,.25);
  }
  .tagline {
    position: absolute; top: 128px; left: 256px; width: 454px;
    font-style: italic; font-size: 22px; line-height: 29px; color: var(--navy);
    text-align: justify;
  }
  .bubble {
    position: absolute; left: 24px; width: 120px; height: 120px; border-radius: 50%;
    background: var(--orange); display: flex; align-items: center; justify-content: center;
    text-align: center; font-size: 16px; line-height: 21px;
  }
  .bubble--send { top: 84px; background: var(--orange-soft); }
  .bubble--receive { top: 182px; padding-top: 2px; }
  .bubble--receive .join { display: block; margin-bottom: 4px; }
  .services-heading {
    position: absolute; top: 228px; left: 160px; width: 410px; text-align: center;
  }
  .services-heading h2 { font-family: "Anton", sans-serif; font-weight: 400; font-size: 30px; letter-spacing: .5px; }
  .services-heading p { font-size: 21px; margin-top: 2px; }
  .step-badge {
    position: absolute; left: 734px; width: 72px; height: 72px; border-radius: 50%;
    background: var(--orange); font-family: "Anton", sans-serif; font-size: 48px;
    display: flex; align-items: center; justify-content: center;
  }
  .steps { position: absolute; list-style: none; }
  .steps li { position: relative; padding-left: 20px; font-size: 21.5px; line-height: 28px; font-weight: 300; }
  .steps li::before { content: "•"; position: absolute; left: 2px; }
  .steps u { text-underline-offset: 3px; }
  .steps--alert { top: 316px; left: 28px; width: 418px; }
  .steps--alert li { text-align: justify; margin-bottom: 6px; }
  .steps--manual { top: 842px; left: 28px; width: 800px; }
  .steps--manual li { margin-bottom: 6px; }
  .steps--fax { top: 1036px; left: 28px; width: 800px; }
  .band-title {
    position: absolute; left: 0; width: 849px; text-align: center; font-weight: 700; font-size: 21px;
  }
  .screen {
    position: absolute; left: 462px; width: 360px; border: 2px solid #8f979f; border-radius: 6px;
    background: linear-gradient(180deg, #e4e7ea, var(--panel));
  }
  .contact {
    position: absolute; top: 1088px; left: 48px; color: var(--navy);
  }
  .contact h3 { font-family: "Anton", sans-serif; font-weight: 400; font-size: 25px; letter-spacing: .5px; }
  .contact p { font-size: 15.5px; line-height: 20px; color: #1c2b3a; }
  .motto {
    position: absolute; top: 1096px; left: 470px; font-style: italic; font-size: 22px; line-height: 30px; color: var(--navy);
  }
</style>
</head>
<body>
<div class="flyer">
  <svg class="backdrop" width="849" height="1200" viewBox="0 0 849 1200" aria-hidden="true">
    <rect width="849" height="1200" fill="#3a7bbf"/>
    <rect y="304" width="849" height="480" fill="#4a86c4"/>
    <polygon points="0,0 849,0 849,72 720,106 0,106" fill="#0455a3"/>
    <polygon points="0,128 60,106 849,72 849,104 760,216 0,216" fill="#dadee3"/>
    <polygon points="0,106 60,106 0,128" fill="#3176b5"/>
    <polygon points="0,216 580,216 580,304 0,304" fill="#0455a3"/>
    <polygon points="0,270 60,216 120,216 0,304" fill="#2a6db1"/>
    <polygon points="580,216 849,216 849,240 720,304 580,304" fill="#dadee3"/>
    <rect x="570" y="216" width="10" height="88" fill="#f37122"/>
    <rect y="784" width="849" height="56" fill="#2f72b6"/>
    <polygon points="0,788 849,788 849,828 0,828" fill="#0455a3"/>
    <polygon points="700,788 849,750 849,788" fill="#dadee3"/>
    <rect y="960" width="849" height="76" fill="#2f72b6"/>
    <polygon points="0,980 849,980 849,1024 0,1024" fill="#0455a3"/>
    <polygon points="720,980 849,950 849,980" fill="#dadee3"/>
    <rect y="1072" width="849" height="128" fill="#dadee3"/>
    <rect y="1080" width="376" height="92" fill="#f68d4c"/>
    <polygon points="0,1172 60,1172 0,1200" fill="#f37122"/>
    <rect x="378" y="1080" width="10" height="92" fill="#0455a3"/>
    <path d="M250 480 C330 440 420 440 470 455" fill="none" stroke="#2a3b4c" stroke-width="2.5" stroke-dasharray="8 6"/>
    <path d="M468 468 C560 490 640 490 690 470" fill="none" stroke="#2a3b4c" stroke-width="2.5" stroke-dasharray="8 6"/>
    <path d="M185 632 C300 622 400 640 470 650" fill="none" stroke="#2a3b4c" stroke-width="2.5" stroke-dasharray="8 6"/>
  </svg>

  <h1 class="title">Brightpath Care HMR</h1>
  <p class="tagline">“ We provide Home Medicine Reviews (HMR) for General Practitioners (GP) at medical centres “</p>

  <div class="bubble bubble--send">Send us<br>a referral for<br>your Patient</div>
  <div class="bubble bubble--receive"><div><span class="join">and</span>Receive a<br>report back<br>with the<br>HMR</div></div>

  <div class="services-heading">
    <h2>How to use our services</h2>
    <p>There are 3 pathways</p>
  </div>
  <div class="step-badge" style="top:232px">1</div>

  <ul class="steps steps--alert">
    <li>Open <u>Patient File</u> in medical prescribing software.</li>
    <li>If patient is eligible for a HMR, an alert will pop up in bottom right hand corner (approx 30 seconds).</li>
    <li>Click <u>Send Referral</u>.</li>
    <li>New page opens, select reason for referral (ie. several medicines).</li>
    <li>Press <u>Send</u> - referral is sent via an encrypted secure electronic transmission to Pharmacis.</li>
    <li>HMR Pharmacist receives referral and conducts interview.</li>
    <li>GP Receives Medication Management Plan - Review and Claim MBS 900</li>
  </ul>

  <div class="screen" style="top:316px;height:170px" role="img" aria-label="Screenshot of the HMR eligibility alert window with Don't Refer, Send Referral and Disable Alerts buttons"></div>
  <div class="screen" style="top:502px;height:160px" role="img" aria-label="Screenshot of the secure referral message form with clinical reason checkboxes"></div>
  <div class="screen" style="top:680px;height:48px" role="img" aria-label="Screenshot of the desktop tray showing the bell icon next to the clock"></div>

  <div class="band-title" style="top:794px">No alert pops up?</div>
  <div class="step-badge" style="top:750px">2</div>
  <ul class="steps steps--manual">
    <li>Right click <u>RX Notify</u> program (the bell shape icon in the bottom right side of the desktop tray next to the time).</li>
    <li>Click <u>Refer Current Patient</u> - this will refer the patient currently open on the GP prescribing software.</li>
  </ul>

  <div class="band-title" style="top:988px">Send via Fax?</div>
  <div class="step-badge" style="top:944px">3</div>
  <ul class="steps steps--fax">
    <li>Send HMR Referal at Fax number: &nbsp;03 9172 3408.</li>
  </ul>

  <div class="contact">
    <h3>Keep in contact</h3>
    <p>brightpathcarehmr@mailvista.example<br>Fax: 03 9172 3408</p>
  </div>
  <p class="motto">Brightpath Care HMR ..<br>Improving Patient Outcomes</p>
</div>
</body>
</html>
```